Coffeeshop menu for filter tip

We want to have a cannabis (coffeeshop) menu in the size 25mm wide x 60mm wide. Some examples attached.

it must have the following text:
Menu

WEED p/g
Velotrine €16
Cinderfox €14
Tide Rambler €14
Marigolden €16
Grand Pelican €14
Copper Comet €14

HASH p/g
Baltic Ember €12
Harbor Velvet€11
Plum Rova €14
Dusk Maple €10

Target Market(s)

tourist in Amsterdam

Requirements
Nice to have
• cannabis sign leaf
• No Cigarettes allowed symbol

```html
<!DOCTYPE html>
<html lang="en">
<head>
<meta charset="utf-8">
<title>Coffeeshop Menu</title>
<link rel="stylesheet" href="https://fonts.googleapis.com/css2?family=Oswald:wght@500&family=Roboto+Condensed:wght@300;400;700&family=Yellowtail&display=swap">
<style>
  :root {
    --page-bg: #e3e3e3;
    --header-bg: #1e2823;
    --body-bg: #0d1712;
    --gold-light: #fbd955;
    --gold-mid: #e6b52c;
    --gold-dark: #b8841a;
    --text-light: #f4f4f2;
    --badge-text: #141414;
    --ban-red: #d32027;
  }
  * { margin: 0; padding: 0; box-sizing: border-box; }
  html, body {
    width: 1200px; height: 2457px; overflow: hidden;
    background: var(--page-bg);
  }
  .menu-card {
    position: absolute; left: 138px; top: 125px;
    width: 927px; height: 2208px;
    background: var(--body-bg);
    box-shadow: 6px 8px 14px rgba(0,0,0,0.35);
    overflow: hidden;
    font-family: "Roboto Condensed", sans-serif;
    color: var(--text-light);
  }
  .menu-header {
    position: absolute; left: 0; top: 0; width: 100%; height: 758px;
    background: var(--header-bg);
  }
  .leaf-emblem {
    position: absolute; left: 200px; top: 104px; width: 519px; height: 485px;
    border-radius: 50% 50% 40% 40%;
    background: linear-gradient(160deg, var(--gold-light), var(--gold-mid) 55%, var(--gold-dark));
  }
  .menu-title {
    position: absolute; left: 150px; width: 627px; top: 580px;
    display: flex; justify-content: space-between;
    font-family: "Oswald", sans-serif; font-weight: 500;
    font-size: 120px; line-height: 1;
    background: linear-gradient(180deg, var(--gold-light), var(--gold-dark));
    -webkit-background-clip: text; background-clip: text; color: transparent;
  }
  .no-smoking-badge { position: absolute; right: 0; top: 0; width: 377px; height: 377px; }
  .section-head {
    position: absolute; left: 83px; right: 91px;
    display: flex; justify-content: space-between; align-items: baseline;
  }
  .section-title {
    font-family: "Yellowtail", cursive; font-size: 104px; line-height: 1;
    background: linear-gradient(180deg, var(--gold-light), var(--gold-dark));
    -webkit-background-clip: text; background-clip: text; color: transparent;
    padding-right: 10px;
  }
  .unit { font-weight: 300; font-size: 66px; }
  .price-list { position: absolute; left: 83px; right: 91px; list-style: none; }
  .price-row {
    height: 97.5px; display: flex; justify-content: space-between; align-items: center;
    font-size: 72px; font-weight: 300; line-height: 1;
  }
  .price { font-weight: 700; }
  .weed-head { top: 820px; }
  .weed-list { top: 951px; }
  .hash-head { top: 1620px; }
  .hash-list { top: 1750px; }
</style>
</head>
<body>
  <main class="menu-card">
    <header class="menu-header">
      <div class="leaf-emblem" role="img" aria-label="Golden cannabis leaf emblem"></div>
      <h1 class="menu-title"><span>M</span><span>E</span><span>N</span><span>U</span></h1>
      <svg class="no-smoking-badge" viewBox="0 0 377 377" role="img" aria-label="No cigarettes allowed">
        <defs>
          <linearGradient id="badgeGold" x1="0" y1="0" x2="1" y2="1">
            <stop offset="0" stop-color="#fbd955"/>
            <stop offset="1" stop-color="#d39e22"/>
          </linearGradient>
        </defs>
        <polygon points="0,0 377,0 377,377" fill="url(#badgeGold)"/>
        <text x="182" y="120" transform="rotate(45 182 120)" text-anchor="middle"
              font-family="Roboto Condensed, sans-serif" font-weight="700" font-size="38"
              fill="#141414">NO CIGARETTES</text>
        <circle cx="281" cy="78" r="50" fill="#1a1a1a"/>
        <rect x="245" y="70" width="62" height="16" fill="#f4f4f2"/>
        <rect x="307" y="70" width="12" height="16" fill="#e07a2a"/>
        <circle cx="281" cy="78" r="42" fill="none" stroke="#d32027" stroke-width="9"/>
        <line x1="252" y1="49" x2="310" y2="107" stroke="#d32027" stroke-width="9"/>
      </svg>
    </header>

    <section class="menu-section">
      <div class="section-head weed-head"><h2 class="section-title">Weed</h2><span class="unit">p/g</span></div>
      <ul class="price-list weed-list">
        <li class="price-row"><span class="strain">Velotrine</span><span class="price">€16</span></li>
        <li class="price-row"><span class="strain">Cinderfox</span><span class="price">€14</span></li>
        <li class="price-row"><span class="strain">Tide Rambler</span><span class="price">€14</span></li>
        <li class="price-row"><span class="strain">Marigolden</span><span class="price">€16</span></li>
        <li class="price-row"><span class="strain">Grand Pelican</span><span class="price">€14</span></li>
        <li class="price-row"><span class="strain">Copper Comet</span><span class="price">€14</span></li>
      </ul>
    </section>

    <section class="menu-section">
      <div class="section-head hash-head"><h2 class="section-title">Hash</h2><span class="unit">p/g</span></div>
      <ul class="price-list hash-list">
        <li class="price-row"><span class="strain">Baltic Ember</span><span class="price">€12</span></li>
        <li class="price-row"><span class="strain">Harbor Velvet</span><span class="price">€11</span></li>
        <li class="price-row"><span class="strain">Plum Rova</span><span class="price">€14</span></li>
        <li class="price-row"><span class="strain">Dusk Maple</span><span class="price">€10</span></li>
      </ul>
    </section>
  </main>
</body>
</html>
```